Boutique Jewellery Card [UPDATED] Embossing and Foil

Hi Designers,

What will win you this competition is your input on making my card look very professional and classy

Just some overview information.

I am striving to be the most prestigious jeweller going around specialising in custom designed jewellery, engagement rings and repairs on a bigger budget.

I am spending a lot on the printing including thick cards, rounded corners, multi level embossing and foiling.

Front:

I want my entire logo on the front, which I will have embossed and foiled (source file included)
Optional: I also want a lower embossing of a repeating pattern which I am not sure on. I need YOUR input here

Back:

I need you to use your skills and experience to make my details look very important, professional and classy.

The details I need on the back are:

Marcus Delvaney
Your Jewellery Stylist

www.marcusdelvaney.com
0492 836 514
marcus@marcusdelvaney.com

The font MUST match the font/style used in the logo.
Everything else including layout, whether my logo is on the back etc, engrave/endent, foiling etc is what I need your input for
Updates

Project Deadline Extended Reason: I was a bit slow and out of action at the start, but we're almost there, just need a few more days to finalize Added Sunday, November 16, 2014

Target Market(s)

25 - 80 year olds. Fashion concious. Wealthy

Industry/Entity Type

Printing

Contact Information for Business Card

Marcus Delvaney
Your Jewellery Stylist

0492 836 514
marcus@marcusdelvaney.com
www.marcusdelvaney.com
- facebook and instagram logo's

Requirements
Must have
• Must use the font from my logo on the back, or very similar
• My logo on the front
• My details on the back must be the centre of attention, my logo can still be there but is less important.
• Back must include the facebook and instagram logo's
Nice to have
• repeating pattern or monogram

```html
<!DOCTYPE html>
<html lang="en">
<head>
<meta charset="utf-8">
<title>Marcus Delvaney – Business Card</title>
<link rel="stylesheet" href="https://fonts.googleapis.com/css2?family=Questrial&display=swap">
<style>
  :root {
    --stage: #3a3a3a;
    --card: #1f1f1f;
    --emboss: #0f0f0f;
    --foil: #f2f2f2;
    --font: "Questrial", sans-serif;
  }
  * { margin: 0; padding: 0; box-sizing: border-box; }
  html, body { width: 1200px; height: 516px; overflow: hidden; }
  body { background: var(--stage); font-family: var(--font); position: relative; }

  .card {
    position: absolute;
    top: 109px;
    width: 458px;
    height: 265px;
    background: var(--card);
    box-shadow: 0 6px 18px rgba(0,0,0,.45);
  }
  .card--front { left: 119px; }
  .card--back { left: 600px; text-align: center; color: var(--foil); }

  .front-mark {
    position: absolute;
    left: 174px;
    top: 43px;
    width: 110px;
    height: 110px;
    border-radius: 50%;
    background: var(--emboss);
  }
  .front-name {
    position: absolute;
    left: 0; right: 0;
    top: 170px;
    text-align: center;
    color: var(--emboss);
    font-size: 25px;
    letter-spacing: 3.4px;
  }

  .back-name {
    position: absolute;
    left: 0; right: 0;
    top: 118px;
    font-size: 24px;
    letter-spacing: 3.6px;
    line-height: 1;
  }
  .back-tagline {
    position: absolute;
    left: 0; right: 0;
    top: 145px;
    font-size: 10px;
    letter-spacing: 2.6px;
    line-height: 12px;
  }
  .back-contact {
    position: absolute;
    left: 0; right: 0;
    top: 191px;
    list-style: none;
    font-size: 13.5px;
    letter-spacing: 0.8px;
    line-height: 14.5px;
  }
  .back-social {
    position: absolute;
    left: 0; right: 0;
    top: 240px;
    display: flex;
    justify-content: center;
    gap: 6px;
  }
  .social-square { width: 11px; height: 11px; background: var(--foil); }
</style>
</head>
<body>
  <section class="card card--front" aria-label="Card front">
    <div class="front-mark"></div>
    <p class="front-name">MARCUS DELVANEY</p>
  </section>

  <section class="card card--back" aria-label="Card back">
    <h1 class="back-name">MARCUS DELVANEY</h1>
    <p class="back-tagline">Specialising in Custom Designed<br>Engagement Rings and Jewellery</p>
    <ul class="back-contact">
      <li>0492 836 514</li>
      <li>marcus@marcusdelvaney.com</li>
      <li>www.marcusdelvaney.com</li>
    </ul>
    <div class="back-social">
      <span class="social-square"></span>
      <span class="social-square"></span>
    </div>
  </section>
</body>
</html>
```